Dance school needs a poster to promote our annual concert

I have a dance school called 'The Marcella Dunwoody Dancers'
See designs from previous years
This year's concert theme is Brant Holloway animation movies
The title of the concert is "glimmeRa"
Dance items will be choreographed to; “Quiet Orchard”, Copper Heron”, “The Nine Lanterns”, “The Fox Regent”, “Temrik”, “Willow & the Warden” & “Pipsqueeve”.
I need a colorful A4 (portrait) poster promoting the concert.

Target Market(s)

Families of students & dance community

Industry/Entity Type

Dance Studio

Font styles to use
Other font styles liked:
• "Mistral" for my my name (see examples supplied)

Colors

Designer to choose colors to be used in the design.

Requirements
Must have
• Must Have:
• - The poster must include the following information:
• 'The Marcella Dunwoody Dancers'
• presents
• "glimmeRa"
• (Font for my name is "Mistral")
• Saturday 18th November 2017
• Corbett Hall,
• Halverd Grammar Elmstead.

```html
<!DOCTYPE html>
<html lang="en">
<head>
<meta charset="utf-8">
<title>glimmeRa – The Marcella Dunwoody Dancers</title>
<link rel="stylesheet" href="https://fonts.googleapis.com/css2?family=Kaushan+Script&family=Great+Vibes&family=Cinzel:wght@500&family=Oswald:wght@600&family=Bowlby+One+SC&family=Archivo+Narrow:wght@600&display=swap">
<style>
  :root {
    --night: #3a1d4a;
    --plum: #6b2a5e;
    --ember: #e0572a;
    --amber: #f6a531;
    --rose: #c73a5c;
    --cream: #fbeedd;
    --wine: #8a1526;
    --gold: #ffd21e;
    --ink: #2c1538;
    --white: #ffffff;
  }
  * { margin: 0; padding: 0; box-sizing: border-box; }
  html, body { width: 849px; height: 1200px; overflow: hidden; background: var(--night); }
  .poster {
    position: relative;
    width: 849px;
    height: 1200px;
    overflow: hidden;
  }
  .backdrop {
    position: absolute;
    inset: 0;
    background:
      radial-gradient(circle at 30% 40%, rgba(246,165,49,.85) 0, rgba(246,165,49,0) 38%),
      radial-gradient(circle at 70% 60%, rgba(224,87,42,.8) 0, rgba(224,87,42,0) 40%),
      radial-gradient(circle at 20% 75%, rgba(199,58,92,.75) 0, rgba(199,58,92,0) 35%),
      radial-gradient(circle at 80% 25%, rgba(199,58,92,.6) 0, rgba(199,58,92,0) 30%),
      linear-gradient(180deg, var(--night) 0%, var(--plum) 22%, var(--ember) 50%, var(--plum) 78%, var(--night) 100%);
  }
  .brand {
    position: absolute;
    top: 18px;
    left: 0;
    width: 100%;
    display: flex;
    justify-content: center;
  }
  .brand-mark {
    width: 68px;
    height: 68px;
    border-radius: 50%;
    background: var(--night);
    display: flex;
    align-items: center;
    justify-content: center;
    font-family: "Kaushan Script", cursive;
    font-size: 26px;
    color: var(--white);
  }
  .school-name {
    position: absolute;
    top: 86px;
    width: 100%;
    text-align: center;
    font-family: "Kaushan Script", cursive;
    font-size: 44px;
    color: var(--white);
  }
  .presents {
    position: absolute;
    top: 148px;
    width: 100%;
    text-align: center;
    font-family: "Cinzel", serif;
    font-size: 34px;
    letter-spacing: 12px;
    color: var(--white);
  }
  .title-disc {
    position: absolute;
    left: 198px;
    top: 296px;
    width: 454px;
    height: 454px;
    border-radius: 50%;
    border: 7px solid var(--white);
    background: radial-gradient(circle, rgba(251,238,221,.95) 0%, rgba(251,238,221,.8) 55%, rgba(246,165,49,.55) 100%);
    display: flex;
    align-items: center;
    justify-content: center;
  }
  .title-disc::after {
    content: "";
    position: absolute;
    inset: 16px;
    border-radius: 50%;
    border: 2px solid rgba(255,255,255,.8);
  }
  .show-title {
    font-family: "Great Vibes", cursive;
    font-size: 128px;
    color: var(--wine);
    transform: rotate(-6deg);
  }
  .details {
    position: absolute;
    top: 952px;
    width: 100%;
    text-align: center;
  }
  .date {
    font-family: "Oswald", sans-serif;
    font-size: 52px;
    color: var(--gold);
    letter-spacing: 1px;
    line-height: 1.1;
  }
  .date sup { font-size: 26px; }
  .venue {
    font-family: "Bowlby One SC", sans-serif;
    font-size: 52px;
    color: var(--ink);
    line-height: 1.15;
    margin-top: 4px;
  }
  .school {
    font-family: "Archivo Narrow", sans-serif;
    font-size: 40px;
    color: var(--white);
    line-height: 1.2;
  }
</style>
</head>
<body>
  <main class="poster">
    <div class="backdrop" role="img" aria-label="Abstract layered geometric shapes in orange, red and purple with glowing bokeh dots and star-like connecting lines"></div>

    <div class="brand"><div class="brand-mark">MDD</div></div>
    <h2 class="school-name">The Marcella Dunwoody Dancers</h2>
    <p class="presents">PRESENTS</p>

    <div class="title-disc">
      <h1 class="show-title">glimmeRa</h1>
    </div>

    <div class="details">
      <p class="date">SATURDAY 18<sup>TH</sup> NOVEMBER 2017</p>
      <p class="venue">CORBETT HALL</p>
      <p class="school">HALVERD GRAMMAR ELMSTEAD</p>
    </div>
  </main>
</body>
</html>
```